Pellmark Ridgeway LLC stationery, business card and web page design.

i need a full set of stationery designed using the name "Pellmark Ridgeway LLC" with a tag line "construction consulting services". using the uploaded monkey icon as the logo.

i like the colors orange, green and black in general but im not limited to that. the company offers consulting services to various types of construction businesses.

i travel around the country in a 4x4 camper offering consulting services and technical training short term and long to various types of construction companies.

Construction Company

Peter Lund
p.lund@pellmarkridgeway.example
2748 Fenwick Rd
Maple Glen, NY 10943
555 014 3627

list these services on the card.

Business Consulting
Capital Investments
Marketing Implementations
Technical Training

1 page

Designer to choose colors to be used in the design.

• company info and use of the monkey icon i provided.
• a fun but professional design
• the color red

```html
<!DOCTYPE html>
<html lang="en">
<head>
<meta charset="utf-8">
<title>Pellmark Ridgeway LLC – Business Card</title>
<link rel="stylesheet" href="https://fonts.googleapis.com/css2?family=Cinzel:wght@500;600&family=Roboto:wght@400;500&display=swap">
<style>
  :root {
    --backdrop: #2b2b2b;
    --brand-orange: #f15a22;
    --card-white: #f2f2f2;
    --ink: #141414;
  }
  * { margin: 0; padding: 0; box-sizing: border-box; }
  html, body { width: 1200px; height: 960px; overflow: hidden; }
  body { background: var(--backdrop); position: relative; font-family: "Roboto", Arial, sans-serif; color: var(--ink); }

  .card {
    position: absolute; left: 299px; width: 600px; height: 342px;
    border-radius: 18px;
  }
  .card--front { top: 137px; background: var(--brand-orange); }
  .card--back  { top: 488px; background: var(--card-white); }

  .front-wordmark {
    position: absolute; left: 60px; top: 136px; width: 210px;
    text-align: center; font-family: "Cinzel", Georgia, serif;
    font-weight: 600; font-size: 26px; line-height: 1.2; color: var(--ink);
  }
  .divider {
    position: absolute; left: 290px; top: 72px; width: 1px; height: 222px;
    background: rgba(20,20,20,.7);
  }
  .details { position: absolute; left: 323px; top: 70px; }
  .person-name { font-family: "Cinzel", Georgia, serif; font-weight: 600; font-size: 26px; line-height: 30px; }
  .person-role { font-family: "Cinzel", Georgia, serif; font-weight: 600; font-size: 15.5px; line-height: 18px; }
  .company { font-weight: 500; font-size: 14px; margin-top: 7px; line-height: 18px; }
  .address { font-size: 14.5px; line-height: 18px; }
  .contact-list { list-style: none; margin-top: 9px; }
  .contact-list li { display: flex; align-items: center; font-size: 14.5px; height: 19.2px; }
  .contact-list svg { width: 13px; height: 13px; margin-right: 10px; fill: var(--ink); flex: none; }

  .back-mark {
    position: absolute; left: 218px; top: 58px; width: 166px; height: 166px;
    border-radius: 50%; background: var(--ink);
  }
  .back-name {
    position: absolute; left: 0; right: 0; top: 241px; text-align: center;
    font-family: "Cinzel", Georgia, serif; font-weight: 500; font-size: 25px; color: var(--brand-orange);
  }
  .back-tagline {
    position: absolute; left: 0; right: 0; top: 273px; text-align: center;
    font-family: "Cinzel", Georgia, serif; font-weight: 600; font-size: 13.5px; color: var(--ink);
  }
</style>
</head>
<body>
  <section class="card card--front">
    <div class="front-wordmark">Pellmark<br>Ridgeway</div>
    <div class="divider"></div>
    <div class="details">
      <p class="person-name">PETER LUND</p>
      <p class="person-role">CEO/FOUNDER</p>
      <p class="company">Pellmark Ridgeway LLC</p>
      <p class="address">2748 Fenwick Rd<br>Maple Glen, NY 10943</p>
      <ul class="contact-list">
        <li><svg viewBox="0 0 16 16"><path d="M3 1l3 3-1.5 2a9 9 0 0 0 5.5 5.5L12 10l3 3-2 2C7 15 1 9 1 3z"/></svg>555 014 3627</li>
        <li><svg viewBox="0 0 16 16"><path d="M4 0h8v16H4zM5.5 2v10h5V2z"/></svg>555 014 3628</li>
        <li><svg viewBox="0 0 16 16"><path d="M4 1h8v4H4zM1 6h14v7h-2v-3H3v3H1zM4 11h8v4H4z"/></svg>555 014 3690</li>
        <li><svg viewBox="0 0 16 16"><path d="M1 3h14v1L8 9 1 4zM1 6l7 5 7-5v7H1z"/></svg>p.lund@pellmarkridgeway.example</li>
        <li><svg viewBox="0 0 16 16"><circle cx="8" cy="8" r="7"/></svg>www.pellmarkridgeway.example</li>
      </ul>
    </div>
  </section>

  <section class="card card--back">
    <div class="back-mark" aria-hidden="true"></div>
    <p class="back-name">PELLMARK RIDGEWAY LLC</p>
    <p class="back-tagline">CONSTRUCTION CONSULTING SERVICES</p>
  </section>
</body>
</html>
```